Zelo Pim

Need
Sexy image with girls dancing around my photo or background white and my photo cropped with the background out and then
Zelo
Pim
Body
Mami

in red , I am looking for a huge Club feel
and I am open for new concepts but that should be a good start.

Target Market(s)

World Wide Appeal

Industry/Entity Type

Club

Requirements
Must have
• 1600 x 1600

Nice to have
• Women, concert crow club something unique royalty free images
Should not have
• nude or obscene photo's

```html
<!DOCTYPE html>
<html lang="en">
<head>
<meta charset="utf-8">
<title>Zelo Pim Body Mami</title>
<link rel="stylesheet" href="https://fonts.googleapis.com/css2?family=Monoton&family=Josefin+Sans:wght@700&family=Arimo&display=swap">
<style>
  :root {
    --page-bg: #efe9ea;
    --club-dark: #2a0a2e;
    --club-magenta: #c21fb4;
    --club-pink: #f06ee0;
    --club-light: #ffd6f6;
    --title-white: #ffffff;
    --pill-magenta: #a3156f;
    --disc-pink: #e9869e;
    --disc-deep: #b73858;
    --disc-light: #f6c3cf;
    --disc-ink: #2b0a14;
    --suit-dark: #141414;
    --skin-shadow: #3a2a22;
    --dress-black: #1a1012;
    --dress-skin: #c89a86;
  }
  html, body {
    margin: 0;
    width: 1200px;
    height: 843px;
    overflow: hidden;
    background: var(--page-bg);
  }
  .stage {
    position: relative;
    width: 1200px;
    height: 843px;
  }
  .disc {
    position: absolute;
    left: 498px;
    top: 163px;
    width: 500px;
    height: 500px;
    border-radius: 50%;
    background: radial-gradient(circle at 50% 50%, var(--disc-light) 0%, var(--disc-pink) 35%, var(--disc-deep) 75%, var(--disc-pink) 100%);
    box-shadow: inset 0 0 0 3px rgba(255,255,255,0.5);
  }
  .disc-hole {
    position: absolute;
    left: 200px;
    top: 200px;
    width: 100px;
    height: 100px;
    border-radius: 50%;
    background: var(--page-bg);
    box-shadow: 0 0 0 26px rgba(255,255,255,0.35);
  }
  .disc-title {
    position: absolute;
    left: 305px;
    top: 168px;
    width: 190px;
    margin: 0;
    color: var(--disc-ink);
    text-align: left;
    line-height: 1;
  }
  .disc-title .line-outline {
    display: block;
    font-family: "Monoton", cursive;
    font-size: 48px;
    font-weight: 400;
  }
  .disc-title .line-solid {
    display: block;
    font-family: "Josefin Sans", sans-serif;
    font-weight: 700;
    font-size: 34px;
    margin: 4px 0;
  }
  .cover {
    position: absolute;
    left: 246px;
    top: 149px;
    width: 531px;
    height: 527px;
    overflow: hidden;
    background: linear-gradient(180deg, var(--club-dark) 0%, var(--club-magenta) 40%, var(--club-pink) 75%, var(--club-light) 100%);
  }
  .club-scene {
    position: absolute;
    inset: 0;
    background: radial-gradient(ellipse at 60% 35%, rgba(255,120,240,0.55) 0%, rgba(120,20,110,0.2) 60%, transparent 100%);
  }
  .dancers {
    position: absolute;
    left: 253px;
    top: 135px;
    width: 278px;
    height: 366px;
    background: linear-gradient(90deg, rgba(26,16,18,0) 0%, var(--dress-black) 25%, var(--dress-skin) 50%, var(--dress-black) 75%, rgba(26,16,18,0) 100%);
    opacity: 0.6;
    border-radius: 40% 40% 10% 10% / 20% 20% 5% 5%;
  }
  .artist-head {
    position: absolute;
    left: 57px;
    top: 90px;
    width: 158px;
    height: 200px;
    border-radius: 50% 50% 45% 45%;
    background: var(--skin-shadow);
  }
  .artist-body {
    position: absolute;
    left: 0;
    top: 268px;
    width: 398px;
    height: 259px;
    border-radius: 30% 40% 0 0 / 25% 30% 0 0;
    background: var(--suit-dark);
  }
  .cover-title {
    position: absolute;
    z-index: 2;
    left: 0;
    top: 26px;
    width: 100%;
    margin: 0;
    font-family: "Monoton", cursive;
    font-weight: 400;
    color: var(--title-white);
    text-align: center;
    font-size: 76px;
    line-height: 1;
  }
  .cover-subtitle {
    position: absolute;
    z-index: 2;
    left: 222px;
    top: 106px;
    margin: 0;
    font-family: "Monoton", cursive;
    font-weight: 400;
    color: var(--title-white);
    font-size: 54px;
    line-height: 62px;
  }
  .title-pill {
    position: absolute;
    z-index: 2;
    left: 294px;
    top: 445px;
    width: 237px;
    height: 32px;
    border-radius: 16px 0 0 16px;
    background: var(--pill-magenta);
    color: var(--title-white);
    font-family: "Arimo", sans-serif;
    font-size: 17px;
    line-height: 32px;
    padding-left: 40px;
    box-sizing: border-box;
    white-space: nowrap;
  }
</style>
</head>
<body>
<main class="stage">
  <div class="disc">
    <div class="disc-hole"></div>
    <h2 class="disc-title">
      <span class="line-outline">ZELO</span>
      <span class="line-solid">PIM BODY</span>
      <span class="line-outline">MAMI</span>
    </h2>
  </div>

  <section class="cover">
    <div class="club-scene" role="img" aria-label="Nightclub interior lit in magenta and purple with a glowing dance floor"></div>
    <div class="dancers" role="img" aria-label="Two women in black dresses posing on the club dance floor"></div>
    <div class="artist-head" role="img" aria-label="Portrait of the artist in sunglasses"></div>
    <div class="artist-body" role="img" aria-label="The artist's dark suit and striped tie"></div>
    <h1 class="cover-title">ZELO PIM</h1>
    <p class="cover-subtitle">BODY<br>MAMI</p>
    <div class="title-pill">Zelo Pim Body Mami</div>
  </section>
</main>
</body>
</html>
```